Flyer for Pharmacy/Medical Convention

Tri-fold flyer for pharmacy/medical convention. The inside of the flyer we would like to look like a venn diagram, possibly using an image similar to our blue logo

Copy write will be submitted when a design is chosen

there will be a flap about educational features, one about supplements an automated recommendations, and a flap about a computer platform to manage patients

Target Market(s)

Pharmacists and Medical Providers

Industry/Entity Type

Supplement

Colors

Designer to choose colors to be used in the design.

Requirements
Must have
• color scheme similar to logos and or label design attached

```html
<!DOCTYPE html>
<html lang="en">
<head>
<meta charset="utf-8">
<title>Tri-fold Flyer – Inside Spread</title>
<link href="https://fonts.googleapis.com/css2?family=Lato:wght@400;700;900&display=swap" rel="stylesheet">
<style>
  :root {
    --backdrop: #8fcbed;
    --paper: #ffffff;
    --royal: #3d4fbf;
    --royal-deep: #2e3fa8;
    --teal: #2fd0da;
    --teal-soft: rgba(47, 208, 218, 0.82);
    --navy: #1d2a6e;
    --bullet: #4a57c9;
    --fold: rgba(0, 0, 0, 0.06);
    --photo-light: #e4e6e8;
    --photo-mid: #a9aeb3;
  }
  * { margin: 0; padding: 0; box-sizing: border-box; }
  html, body { width: 1200px; height: 900px; overflow: hidden; }
  body {
    background: var(--backdrop);
    font-family: "Lato", Arial, sans-serif;
    position: relative;
  }
  .brochure {
    position: absolute;
    left: 50px; top: 70px;
    width: 1100px; height: 760px;
    background: var(--paper);
    overflow: hidden;
    box-shadow: 0 18px 40px rgba(20, 60, 110, 0.25);
  }
  .brochure__art { position: absolute; inset: 0; }
  .panel-copy { position: absolute; color: #fff; }
  .panel-copy--left { left: 56px; top: 318px; width: 270px; }
  .panel-copy--middle { left: 410px; top: 120px; width: 300px; color: var(--navy); }
  .panel-heading { font-weight: 900; font-size: 25px; line-height: 1.05; }
  .panel-subheading { font-weight: 700; font-size: 17px; margin-bottom: 16px; }
  .panel-body { font-size: 13.5px; line-height: 1.5; }
  .feature-list { list-style: none; margin-top: 4px; }
  .feature-list li {
    position: relative; padding-left: 22px;
    font-size: 14px; line-height: 1.72; font-weight: 700;
  }
  .feature-list li::before {
    content: ""; position: absolute; left: 2px; top: 8px;
    width: 8px; height: 8px; border-radius: 50%; background: var(--bullet);
  }
  .call-block { margin-top: 20px; color: #fff; }
  .call-label { font-size: 20px; font-weight: 700; }
  .call-number { display: flex; align-items: center; gap: 10px; font-size: 30px; font-weight: 700; line-height: 1; }
  .call-icon { width: 24px; height: 24px; }
</style>
</head>
<body>
  <div class="brochure">
    <svg class="brochure__art" width="1100" height="760" viewBox="0 0 1100 760">
      <defs>
        <linearGradient id="portrait-tone" x1="0" y1="0" x2="1" y2="1">
          <stop offset="0" stop-color="#f1f2f3"/>
          <stop offset="1" stop-color="#b8bdc2"/>
        </linearGradient>
        <linearGradient id="lab-tone" x1="0" y1="0" x2="1" y2="1">
          <stop offset="0" stop-color="#c9e3f2"/>
          <stop offset="1" stop-color="#6f8fa8"/>
        </linearGradient>
        <linearGradient id="product-tone" x1="0" y1="0" x2="0" y2="1">
          <stop offset="0" stop-color="#2b2f3a"/>
          <stop offset="1" stop-color="#0f1116"/>
        </linearGradient>
      </defs>

      <rect class="portrait-photo" x="733" y="0" width="367" height="760" fill="url(#portrait-tone)"
            role="img" aria-label="Black and white photo of a senior doctor in a laboratory"/>

      <circle class="venn-circle venn-circle--royal" cx="250" cy="610" r="400" fill="var(--royal)"/>
      <circle class="venn-circle venn-circle--teal" cx="570" cy="330" r="375" fill="var(--teal-soft)"/>

      <circle class="lab-photo" cx="830" cy="230" r="112" fill="url(#lab-tone)" stroke="#fff" stroke-width="7"
              role="img" aria-label="Photo of a scientist working with lab samples"/>
      <circle class="lab-photo" cx="905" cy="470" r="78" fill="url(#lab-tone)" stroke="#fff" stroke-width="6"
              role="img" aria-label="Photo of a researcher using a microscope"/>

      <rect class="product-photo" x="150" y="555" width="210" height="150" rx="10" fill="url(#product-tone)"
            role="img" aria-label="Photo of supplement powder tubs"/>

      <rect class="fold-line" x="366" y="0" width="2" height="760" fill="var(--fold)"/>
      <rect class="fold-line" x="733" y="0" width="2" height="760" fill="var(--fold)"/>
    </svg>

    <div class="panel-copy panel-copy--left">
      <h2 class="panel-heading">Lorem ipsum dolor</h2>
      <p class="panel-subheading">Sit amet, consectetur</p>
      <p class="panel-body">Interdum et malesuada fames ac ante ipsum primis in faucibus. Curabitur venenatis tristique ipsum. Cras sollicitudin lectus sem, id tempus sapien posuere at. Proin ac elementum ante. Mauris ut metus ut metus vehicula cursus et non ipsum. Cras ullamcorper pellentesque nisl, vitae dictum urna fringilla vitae.</p>
    </div>

    <div class="panel-copy panel-copy--middle">
      <h2 class="panel-heading">Lorem ipsum dolor</h2>
      <p class="panel-subheading">Sit amet, consectetur</p>
      <ul class="feature-list">
        <li>Cras vel augue ut nulla auctor</li>
        <li>tincidunt ut et leo.</li>
        <li>In id diam accumsan, tincidunt</li>
        <li>tellus ut, consequat libero.</li>
        <li>Quisque cursus erat dapibus</li>
        <li>accumsan luctus.</li>
        <li>Morbi quis elit eleifend,</li>
        <li>Duis tristique leo non</li>
        <li>Sed nec mauris sagittis, euismod</li>
        <li>sem ac, consectetur sem.</li>
        <li>Cras vel arcu quis ex</li>
        <li>Vivamus euismod nulla maenetus</li>
      </ul>
      <div class="call-block">
        <p class="call-label">Call Us</p>
        <p class="call-number">
          <svg class="call-icon" viewBox="0 0 24 24">
            <circle cx="12" cy="12" r="12" fill="var(--bullet)"/>
            <path d="M8.2 6.5l2 2.3-1.1 1.6c.8 1.7 2 2.9 3.7 3.7l1.6-1.1 2.3 2-.9 2c-4.6-.4-8.2-4-8.6-8.6z" fill="#fff"/>
          </svg>
          1234567890
        </p>
      </div>
    </div>
  </div>
</body>
</html>
```